Heron Haulage Ltd

We need an A5 size (UK size) flyer to advertise our new business which is called Heron Haulage.
Domestic and Commercial Waste Clearance Services.
Please have the question in bold "Do you have a pile of junk you need to dispose of?"
We collect all kinds of junk or rubbish from homes and businesses across Kent, Sussex and South London.
No fuss, no mess!
A low cost, hassle free alternative to skip hire.
Licensed by the Landcare Board and fully insured (this can be in small print at the bottom).
Please put the Recycle symbol somewhere.
Our tagline on our vehicle is "We Clear More, For Less!"
We'd like the flyer to be bold and eye-catching (to catch the eye of the homeowner or business owner while it's sitting on their doormat).
We need our telephone, website and email to be prominent. Maybe saying "Call today for a free quote"
Tel. 01734 580916
Email: info@heronhaulage.example
www.heronhaulage.example
Target Market(s)
Our market will be homes and small businesses around Kent, Sussex and South London.
Industry/Entity Type
Business
Font styles to use
Look and feel

```html
<!DOCTYPE html>
<html lang="en">
<head>
<meta charset="utf-8">
<title>Heron Haulage – Waste Clearance Flyer</title>
<link rel="stylesheet" href="https://fonts.googleapis.com/css2?family=Lato:ital,wght@0,400;0,700;1,700&family=Open+Sans:ital,wght@0,400;1,400&family=Roboto:wght@400&display=swap">
<style>
  :root {
    --brand-green: #27ae58;
    --navy: #2b2468;
    --ink: #1e1e1e;
    --logo-grey: #58595b;
    --white: #ffffff;
    --page: #f2f2f2;
  }
  html, body {
    margin: 0;
    padding: 0;
    width: 1200px;
    height: 876px;
    overflow: hidden;
    background: var(--page);
  }
  .canvas {
    position: relative;
    width: 1200px;
    height: 876px;
    overflow: hidden;
  }
  .flyer {
    position: absolute;
    left: 0;
    top: 0;
    width: 1378px;
    height: 970px;
    transform: scale(0.8708, 0.9031);
    transform-origin: 0 0;
    overflow: hidden;
    font-family: "Lato", Arial, sans-serif;
  }
  .flyer-backdrop {
    position: absolute;
    inset: 0;
  }
  .flyer-shapes {
    position: absolute;
    inset: 0;
    width: 1378px;
    height: 970px;
  }
  .headline {
    position: absolute;
    left: 46px;
    top: 44px;
    margin: 0;
    font-weight: 700;
    font-size: 60px;
    letter-spacing: -0.5px;
    color: var(--brand-green);
  }
  .question {
    position: absolute;
    left: 46px;
    top: 132px;
    margin: 0;
    font-weight: 400;
    font-size: 40px;
    line-height: 50px;
    color: var(--navy);
  }
  .services {
    position: absolute;
    left: 46px;
    top: 245px;
    font-family: "Roboto", Arial, sans-serif;
    font-size: 21.5px;
    line-height: 35px;
    color: var(--ink);
  }
  .services p { margin: 0 0 9px; }
  .brand-name {
    position: absolute;
    left: 880px;
    top: 78px;
    width: 460px;
    text-align: center;
    font-family: "Lato", Arial, sans-serif;
    font-weight: 700;
    color: var(--logo-grey);
  }
  .brand-name .primary {
    display: block;
    font-size: 92px;
    line-height: 100px;
    letter-spacing: 6px;
  }
  .brand-name .secondary {
    display: block;
    font-size: 32px;
    letter-spacing: 30px;
    margin-left: 30px;
  }
  .recycle-mark {
    position: absolute;
    left: 978px;
    top: 322px;
    width: 235px;
    height: 225px;
    border-radius: 22px;
    background: radial-gradient(circle at 50% 45%, #8ed86b 0%, #3fae3a 55%, #1f7f2c 100%);
    border: 6px solid var(--white);
  }
  .call-panel {
    position: absolute;
    right: 40px;
    top: 664px;
    text-align: right;
    color: var(--white);
  }
  .cta {
    margin: 0;
    font-family: "Lato", Arial, sans-serif;
    font-weight: 700;
    font-style: italic;
    font-size: 29px;
    line-height: 34px;
    letter-spacing: -0.5px;
  }
  .call-label {
    margin: 26px 0 0;
    font-family: "Open Sans", Arial, sans-serif;
    font-size: 40px;
    line-height: 46px;
  }
  .phone {
    margin: 0;
    font-family: "Open Sans", Arial, sans-serif;
    font-size: 48px;
    line-height: 56px;
    letter-spacing: 0.5px;
    display: flex;
    align-items: center;
    justify-content: flex-end;
    gap: 14px;
  }
  .phone svg { width: 40px; height: 40px; }
  .contact-row {
    position: absolute;
    right: 46px;
    top: 888px;
    display: flex;
    gap: 30px;
    font-family: "Open Sans", Arial, sans-serif;
    font-size: 21px;
    color: var(--white);
  }
  .contact-row span { display: flex; align-items: center; gap: 6px; }
  .contact-row svg { width: 26px; height: 22px; }
  .licence {
    position: absolute;
    right: 46px;
    top: 928px;
    margin: 0;
    font-family: "Open Sans", Arial, sans-serif;
    font-style: italic;
    font-size: 17.5px;
    color: var(--white);
  }
</style>
</head>
<body>
<div class="canvas">
  <div class="flyer">
    <div class="flyer-backdrop" role="img" aria-label="Photograph of old rusted flywheel machinery on a mossy timber frame in a pine forest">
      <svg class="flyer-shapes" viewBox="0 0 1378 970" aria-hidden="true">
        <defs>
          <linearGradient id="photoTone" x1="0" y1="0" x2="1" y2="1">
            <stop offset="0" stop-color="#5f7d5a"/>
            <stop offset="0.45" stop-color="#7e8f78"/>
            <stop offset="0.75" stop-color="#5d4a3c"/>
            <stop offset="1" stop-color="#3f4a36"/>
          </linearGradient>
          <radialGradient id="paperTone" cx="0.45" cy="0.5" r="0.7">
            <stop offset="0" stop-color="#ffffff"/>
            <stop offset="1" stop-color="#e2e3e4"/>
          </radialGradient>
        </defs>
        <rect class="photo-area" x="0" y="330" width="1378" height="640" fill="url(#photoTone)"/>
        <path class="top-panel" d="M0 0 H1378 V343 C1100 420 820 515 500 515 C300 513 130 455 0 388 Z" fill="url(#paperTone)"/>
        <path class="green-sweep" d="M0 858 C120 905 280 930 430 925 C800 905 1150 650 1378 388 V970 H0 Z" fill="var(--brand-green)"/>
      </svg>
    </div>

    <h1 class="headline">We Clear More, For Less!</h1>
    <h2 class="question">Do you have a pile of junk you<br>need to dispose of?</h2>
    <div class="services">
      <p>WE COLLECT ALL KINDS OF JUNK OR RUBBISH FROM HOMES AND BUSINESS.<br>NO FUSS, NO MESS! A LOW COST, HASSLE FREE ALTERNATIVE TO SKIP HIRE.</p>
      <p>WE PROVIDE DOMESTIC AND COMMERCIAL WASTE CLEARANCE<br>SERVICES ACROSS KENT, SUSSEX AND SOUTH LONDON.</p>
    </div>

    <div class="brand-name">
      <span class="primary">HERON</span>
      <span class="secondary">HAULAGE</span>
    </div>

    <div class="recycle-mark" role="img" aria-label="Green recycling arrows illustration wrapped around a globe"></div>

    <div class="call-panel">
      <p class="cta">CALL TODAY FOR A<br>FREE QUOTE</p>
      <p class="call-label">Call Us Now</p>
      <p class="phone">
        <svg viewBox="0 0 40 40" aria-hidden="true">
          <circle cx="20" cy="20" r="17" fill="none" stroke="currentColor" stroke-width="3"/>
          <path d="M14 11 l4 -1 l2 5 l-3 2 c1 3 3 5 6 6 l2 -3 l5 2 l-1 4 c-8 1 -16 -7 -15 -15 z" fill="currentColor"/>
        </svg>
        01734 580916
      </p>
    </div>

    <div class="contact-row">
      <span>
        <svg viewBox="0 0 26 20" aria-hidden="true"><rect x="1" y="2" width="24" height="16" fill="none" stroke="#fff" stroke-width="2"/><path d="M1 2 L13 12 L25 2" fill="none" stroke="#fff" stroke-width="2"/></svg>
        info@heronhaulage.example
      </span>
      <span>
        <svg viewBox="0 0 22 22" aria-hidden="true"><circle cx="11" cy="11" r="9.5" fill="none" stroke="#fff" stroke-width="1.6"/><ellipse cx="11" cy="11" rx="4.5" ry="9.5" fill="none" stroke="#fff" stroke-width="1.4"/><path d="M1.5 11 H20.5 M3 6 H19 M3 16 H19" stroke="#fff" stroke-width="1.4"/></svg>
        www.heronhaulage.example
      </span>
    </div>
    <p class="licence">Licensed by the Landcare Board and fully insured</p>
  </div>
</div>
</body>
</html>
```